Modern Medical Billing Company Services Brochure

We need a brochure for marketing purposes. This brochure will have to captivate our target market which is physicians.
The brochure will be in the form of a mini booklet with measurements 8.5L X 5.5W.
The front page will be created by the designer but should include the company logo and name. The first left inner page should contain the company's about us page which can be found http://www.harborline-bx.com/about/. The first right inner page should contain a table of content of the following services in this precise order:
- Revenue Cycle Management
- uFiler
- ZTQv
- PlumRemit
- MossHarvest
- LinoVera
- VelmaCrest
- oPlexKEY
- ZentaLoop
- GarnetSuitePlus
We will require that the each service both the left and the right side of the booklet as its opened.
The company website is http://www.harborline-bx.com
Healthcare professionals
Health Care

```html
<!DOCTYPE html>
<html lang="en">
<head>
<meta charset="utf-8">
<title>Harborline Brochure Cover Spread</title>
<link rel="stylesheet" href="https://fonts.googleapis.com/css2?family=Lato:wght@400;700;900&family=Oswald:wght@400;600&display=swap">
<style>
  :root {
    --green: #6cc23a;
    --green-dark: #4f9f22;
    --charcoal: #2b2b2b;
    --charcoal-deep: #1c1c1c;
    --band: #333436;
    --paper: #f3f3f3;
    --paper-shade: #dcdcdc;
    --text-grey: #3c3c3c;
    --white: #ffffff;
    --stage: #e6e6e6;
  }
  * { margin: 0; padding: 0; box-sizing: border-box; }
  html, body { width: 1105px; height: 1200px; overflow: hidden; }
  body { background: var(--stage); font-family: "Lato", sans-serif; position: relative; }

  .spread {
    position: absolute; left: 40px; top: 262px;
    width: 1025px; height: 676px;
    box-shadow: 0 6px 24px rgba(0,0,0,0.25);
    overflow: hidden;
  }
  .back-cover {
    position: absolute; left: 0; top: 0; width: 512px; height: 676px;
    background: radial-gradient(ellipse at 45% 40%, #4a4a4a 0%, var(--charcoal) 55%, var(--charcoal-deep) 100%);
  }
  .front-cover {
    position: absolute; left: 512px; top: 0; width: 513px; height: 676px;
    background: linear-gradient(135deg, var(--white) 0%, var(--paper) 60%, var(--paper-shade) 100%);
  }
  .shapes { position: absolute; left: 0; top: 0; }

  .brand {
    position: absolute; display: flex; align-items: center; gap: 10px;
    font-family: "Lato", sans-serif; font-weight: 900;
  }
  .brand-dot { width: 18px; height: 18px; border-radius: 50%; background: var(--green); }
  .brand--back { left: 0; width: 512px; top: 220px; justify-content: center; font-size: 30px; color: var(--white); }
  .brand--front { left: 855px; top: 70px; font-size: 22px; color: var(--text-grey); }

  .contact-list {
    position: absolute; left: 172px; top: 406px; list-style: none;
    color: var(--white); font-size: 16px; line-height: 22px;
  }
  .contact-list li { display: flex; align-items: center; gap: 8px; }
  .contact-list svg { width: 12px; height: 12px; flex: none; }

  .cover-title {
    position: absolute; right: 24px; top: 496px; text-align: right;
  }
  .cover-title__main {
    font-family: "Oswald", sans-serif; font-weight: 600;
    font-size: 50px; line-height: 56px; color: var(--green); letter-spacing: 0.5px;
  }
  .cover-title__sub {
    font-family: "Lato", sans-serif; font-weight: 400;
    font-size: 24px; line-height: 28px; color: var(--text-grey); letter-spacing: 1px;
  }
  .band-phone {
    position: absolute; left: 690px; top: 638px; width: 240px; text-align: center;
    color: var(--white); font-weight: 700; font-size: 18px; letter-spacing: 3px;
  }
</style>
</head>
<body>
  <div class="spread">
    <section class="back-cover"></section>
    <section class="front-cover"></section>

    <svg class="shapes" width="1025" height="676" viewBox="0 0 1025 676">
      <defs>
        <linearGradient id="officePhoto" x1="0" y1="0" x2="1" y2="1">
          <stop offset="0" stop-color="#e9edf1"/>
          <stop offset="0.45" stop-color="#7fa6d1"/>
          <stop offset="1" stop-color="#b79a78"/>
        </linearGradient>
        <linearGradient id="chartPhoto" x1="0" y1="0" x2="1" y2="1">
          <stop offset="0" stop-color="#5d94cf"/>
          <stop offset="0.6" stop-color="#b9d3ec"/>
          <stop offset="1" stop-color="#3f78b8"/>
        </linearGradient>
      </defs>
      <!-- back cover accents -->
      <polygon points="0,0 141,0 0,74" fill="var(--green)"/>
      <!-- front cover bottom band -->
      <rect x="512" y="624" width="513" height="52" fill="var(--band)"/>
      <!-- green foot with rising wedge -->
      <polygon points="0,624 464,624 512,538 594,676 0,676" fill="var(--green)"/>

      <!-- office scene area -->
      <polygon role="img" aria-label="Photo of two medical billing professionals reviewing documents at a desk"
        points="512,0 608,0 823,340 630,623 512,623 512,538" fill="url(#officePhoto)"/>
      <polyline points="616,0 833,340 640,623" fill="none" stroke="var(--green)" stroke-width="7"/>
      <polyline points="630,0 849,340 656,623" fill="none" stroke="var(--band)" stroke-width="10"/>

      <!-- growth chart area -->
      <polygon role="img" aria-label="Photo of a rising bar chart with an upward trend arrow"
        points="801,174 1025,120 1025,470" fill="url(#chartPhoto)"/>
      <polyline points="801,174 1025,120 M801,174 1025,470" fill="none" stroke="var(--green)" stroke-width="4"/>
      <path d="M801,174 L1025,120 M801,174 L1025,470" stroke="var(--green)" stroke-width="4" fill="none"/>
    </svg>

    <div class="brand brand--back"><span class="brand-dot"></span>Harborline</div>

    <ul class="contact-list">
      <li><svg viewBox="0 0 12 12"><path d="M2.5 1 L4.5 1 L5.3 3.5 L4 4.5 Q5 7 7.5 8 L8.5 6.7 L11 7.5 L11 9.5 Q10.5 11 9 11 Q1 10 1 3 Q1 1.5 2.5 1Z" fill="var(--green)"/></svg>(555) 214-6083</li>
      <li><svg viewBox="0 0 12 12"><rect x="1" y="2.5" width="10" height="7" fill="var(--green)"/><path d="M1 2.5 L6 6.5 L11 2.5" stroke="var(--charcoal)" stroke-width="1" fill="none"/></svg>info@harborline-bx.com</li>
      <li><svg viewBox="0 0 12 12"><circle cx="6" cy="6" r="5" fill="var(--green)"/><path d="M1 6 H11 M6 1 Q3 6 6 11 M6 1 Q9 6 6 11" stroke="var(--charcoal)" stroke-width="0.8" fill="none"/></svg>www.harborline-bx.com</li>
    </ul>

    <div class="brand brand--front"><span class="brand-dot"></span>Harborline</div>

    <div class="cover-title">
      <div class="cover-title__main">REVENUE</div>
      <div class="cover-title__sub">MANAGEMENT</div>
    </div>

    <div class="band-phone">555-214-6083</div>
  </div>
</body>
</html>
```